Veterinary Clinic Letterhead - Ridgeline Veterinary Surgery

We need a letterhead design for an established Veterinary Clinic in Brinvale called Ridgeline Veterinary Surgery. We are a moderate sized mixed animal veterinary clinic offering a wide variety of veterinary services. The design should use the same colour pattern as those in the logos supplied. The design should also include our address (58 Corvane Street, Brinvale, Queensland, 4871), phone number (07 4167 5830), email (admin@ridgelinevets.example.au), website (www.ridgelinevets.example.au) and our opening hours (7am to 6pm Monday to Friday and 9am to 1pm Saturday).
Target Market(s)
Pet owners
Industry/Entity Type
Veterinary
Requirements
Must have
- The logo or modification of it, business address, opening hours, website, phone number and email address

```html
<!DOCTYPE html>
<html lang="en">
<head>
<meta charset="utf-8">
<title>Ridgeline Veterinary Surgery – Stationery</title>
<link href="https://fonts.googleapis.com/css2?family=Open+Sans:wght@400&family=Roboto:wght@400;500&family=Montserrat:wght@500&display=swap" rel="stylesheet">
<style>
  :root {
    --navy: #0d2b4e;
    --backdrop: #dedede;
    --paper: #ffffff;
    --body-text: #4a4a4a;
    --footer-text: #3a3a3a;
    --placeholder: #e6e9ee;
  }
  * { margin: 0; padding: 0; box-sizing: border-box; }
  html, body { width: 1200px; height: 800px; overflow: hidden; }
  body { background: var(--backdrop); position: relative; font-family: "Open Sans", sans-serif; }

  .sheet { position: absolute; top: 111px; width: 411px; height: 574px; }

  /* Back cover */
  .cover { left: 165px; background: var(--navy); color: var(--paper); }
  .cover-mark {
    position: absolute; left: 140px; top: 200px; width: 130px; height: 130px;
    border-radius: 50%; background: var(--paper);
  }
  .cover-name {
    position: absolute; left: 0; right: 0; top: 342px; text-align: center;
    font-family: "Montserrat", sans-serif; font-weight: 500; font-size: 20px;
    letter-spacing: 1px; line-height: 1.3; text-transform: uppercase;
  }
  .cover-web {
    position: absolute; left: 0; right: 0; top: 522px; text-align: center;
    font-family: "Roboto", sans-serif; font-size: 14.5px; letter-spacing: .2px;
  }

  /* Letterhead */
  .letter { left: 613px; background: var(--paper); }
  .letter-mark {
    position: absolute; left: 174px; top: 28px; width: 58px; height: 58px;
    border-radius: 50%; background: var(--navy);
  }
  .letter-name {
    position: absolute; left: 0; right: 0; top: 93px; text-align: center;
    font-family: "Montserrat", sans-serif; font-weight: 500; font-size: 9px;
    letter-spacing: .5px; line-height: 1.3; color: var(--navy); text-transform: uppercase;
  }
  .letter-body {
    position: absolute; left: 43px; top: 158px; width: 321px;
    font-size: 7.2px; line-height: 10.6px; color: var(--body-text);
  }
  .letter-body p { text-align: justify; margin-bottom: 10.6px; }
  .letter-body .salutation, .letter-body .closing { text-align: left; }
  .signature {
    position: absolute; left: 43px; top: 434px; width: 48px; height: 46px;
    background: var(--placeholder);
  }
  .contact-list {
    position: absolute; left: 43px; top: 514px; list-style: none;
    font-family: "Roboto", sans-serif; font-size: 8.2px; line-height: 11.3px; color: var(--footer-text);
  }
  .contact-list li { display: flex; align-items: center; gap: 3px; }
  .contact-list svg { width: 8px; height: 8px; fill: var(--navy); }
  .address {
    position: absolute; right: 44px; top: 517px; text-align: right; font-style: normal;
    font-family: "Roboto", sans-serif; font-size: 8.2px; line-height: 10px; color: var(--footer-text);
  }
  .address .address-name { color: var(--navy); }
  .hours-band {
    position: absolute; left: 0; right: 0; bottom: 0; height: 19px;
    background: var(--navy); color: var(--paper); text-align: center;
    font-family: "Roboto", sans-serif; font-weight: 500; font-size: 8.7px; line-height: 19px;
  }
</style>
</head>
<body>

<section class="sheet cover">
  <div class="cover-mark" aria-hidden="true"></div>
  <div class="cover-name">Ridgeline Veterinary<br>Surgery</div>
  <div class="cover-web">www.ridgelinevets.example.au</div>
</section>

<section class="sheet letter">
  <div class="letter-mark" aria-hidden="true"></div>
  <div class="letter-name">Ridgeline Veterinary<br>Surgery</div>

  <div class="letter-body">
    <p class="salutation">Dear customer,</p>
    <p>Lorem ipsum dolor sit amet, consectetur adipisicing elit, sed do eiusmod tempor incididunt ut labore et dolore magna aliqua. Ut enim ad minim veniam, quis nostrud exercitation ullamco laboris nisi ut aliquip ex ea commodo consequat. Duis aute irure dolor in reprehenderit in voluptate velit esse cillum dolore eu fugiat nulla pariatur. Excepteur sint occaecat cupidatat non proident, sunt in culpa qui officia deserunt mollit anim id est laborum.</p>
    <p>Lorem ipsum dolor sit amet, consectetur adipisicing elit, sed do eiusmod tempor incididunt ut labore et dolore magna aliqua. Ut enim ad minim veniam, quis nostrud exercitation ullamco laboris nisi ut aliquip ex ea commodo consequat. Duis aute irure dolor in reprehenderit in voluptate velit esse cillum dolore eu fugiat nulla pariatur. Excepteur sint occaecat cupidatat non proident, sunt in culpa qui officia deserunt mollit anim id est laborum.</p>
    <p>Lorem ipsum dolor sit amet, consectetur adipisicing elit, sed do eiusmod tempor incididunt ut labore et dolore magna aliqua. Ut enim ad minim veniam, quis nostrud exercitation ullamco laboris nisi ut aliquip ex ea commodo consequat. Duis aute irure dolor in reprehenderit in voluptate velit esse cillum dolore eu fugiat nulla pariatur. Excepteur sint occaecat cupidatat non proident, sunt in culpa qui officia deserunt mollit anim id est laborum.</p>
    <p>Lorem ipsum dolor sit amet, consectetur adipisicing elit, sed do eiusmod tempor incididunt ut labore et dolore magna aliqua. Ut enim ad minim veniam, quis nostrud exercitation ullamco laboris nisi ut aliquip ex ea commodo consequat. Duis aute irure dolor in reprehenderit.</p>
    <p class="closing">Yours Sincerely,</p>
  </div>

  <div class="signature" role="img" aria-label="Handwritten signature"></div>

  <ul class="contact-list">
    <li><svg viewBox="0 0 24 24" aria-hidden="true"><path d="M6.6 10.8a15.1 15.1 0 0 0 6.6 6.6l2.2-2.2c.3-.3.7-.4 1-.2 1.1.4 2.3.6 3.6.6.6 0 1 .4 1 1V20c0 .6-.4 1-1 1A17 17 0 0 1 3 4c0-.6.4-1 1-1h3.5c.6 0 1 .4 1 1 0 1.3.2 2.5.6 3.6.1.3 0 .7-.2 1z"/></svg>07 4167 5830</li>
    <li><svg viewBox="0 0 24 24" aria-hidden="true"><path d="M2 5h20v14H2z M4 7v.4l8 5.6 8-5.6V7z" fill-rule="evenodd"/></svg>admin@ridgelinevets.example.au</li>
    <li><svg viewBox="0 0 24 24" aria-hidden="true"><path d="M12 2a10 10 0 1 0 0 20 10 10 0 0 0 0-20zm0 2a8 8 0 0 1 7.7 6h-4.2A13 13 0 0 0 13.8 4.2 8 8 0 0 1 12 4zm-2 .3A12 12 0 0 0 8.5 10H4.3A8 8 0 0 1 10 4.3zM4.3 14h4.2a12 12 0 0 0 1.5 5.7A8 8 0 0 1 4.3 14zm6.2 0h3a11 11 0 0 1-1.5 5 11 11 0 0 1-1.5-5zm0-4a11 11 0 0 1 1.5-5 11 11 0 0 1 1.5 5zm3.3 9.8a13 13 0 0 0 1.7-5.8h4.2a8 8 0 0 1-5.9 5.8z"/></svg>www.ridgelinevets.example.au</li>
  </ul>

  <address class="address">
    <span class="address-name">Ridgeline Veterinary Surgery</span><br>
    58 Corvane Street, Brinvale,<br>
    Queensland, 4871
  </address>

  <div class="hours-band">7am to 6pm Monday to Friday and 9am to 1pm Saturday</div>
</section>

</body>
</html>
```